Bookkeeping website design

We need a basic site design for wordpress.
We are a bookkeeping business and will need to present a look consistent with the colours and style of the logo.

Target Market(s)

Business owners

Industry/Entity Type

Accounting/Bookkeeping

Coding

Coded - Design and coding required

Number of Pages Required

1 page

```html
<!DOCTYPE html>
<html lang="en">
<head>
<meta charset="utf-8">
<title>Ledgerly Bookkeeping</title>
<link href="https://fonts.googleapis.com/css2?family=Marcellus&family=Poppins:wght@300;400;500;600&display=swap" rel="stylesheet">
<style>
:root{
  --blue:#14b3ef;
  --green:#8dc63f;
  --green-soft:#a8d65a;
  --ink:#222;
  --text:#555;
  --muted:#888;
  --line:#e6e6e6;
  --dark:#1b1b1b;
  --white:#fff;
}
*{box-sizing:border-box;margin:0;padding:0}
html,body{width:1200px;height:5300px;overflow:hidden}
body{position:relative;font-family:"Poppins",sans-serif;color:var(--text);background:var(--white);font-size:12px}
.abs{position:absolute}
.serif{font-family:"Marcellus",serif;font-weight:400}
.btn{position:absolute;display:flex;align-items:center;justify-content:center;background:var(--blue);color:var(--white);border-radius:20px;font-size:12px;height:34px;white-space:nowrap}
.photo{position:absolute}
.section-title{position:absolute;left:0;width:1200px;text-align:center;font-family:"Marcellus",serif;font-size:28px;color:var(--ink)}
.section-sub{position:absolute;left:0;width:1200px;text-align:center;font-size:11px;color:var(--text)}

/* header */
.brand{position:absolute;left:124px;top:34px;display:flex;align-items:center;gap:10px;font-family:"Poppins",sans-serif;font-weight:600;font-size:18px;color:var(--green);white-space:nowrap}
.brand .mark{width:30px;height:30px;border-radius:50%;background:var(--blue)}
.nav{position:absolute;top:49px;left:474px;display:flex;gap:34px;font-size:11px;color:#444;white-space:nowrap}
.nav .active{color:var(--green)}
.quote-btn{left:930px;top:40px;width:138px;height:32px;font-size:11px;justify-content:flex-start;padding-left:20px;gap:10px}

/* hero */
.hero{position:absolute;left:0;top:113px;width:1200px;height:680px;overflow:hidden}
.hero-photo{left:0;top:0;width:1200px;height:680px;background:linear-gradient(90deg,#2b2b2b 0%,#3a3a3a 35%,#bdbdbd 55%,#e9e9e9 75%,#d8d8d8 100%)}
.hero-bar{left:172px;top:240px;width:3px;height:100px;background:var(--blue)}
.hero-title{left:195px;top:236px;font-size:50px;line-height:56px;color:var(--white);letter-spacing:1px;white-space:nowrap}
.hero-title span{color:var(--blue);display:block}
.hero-copy{left:195px;top:363px;width:400px;font-size:10.5px;line-height:18px;color:#eee}
.hero-btn{left:195px;top:416px;width:128px;height:32px}
.hero-count{left:1108px;top:296px;color:var(--white);font-size:10px;display:flex;align-items:center;gap:6px}
.hero-count i{display:block;width:46px;height:1px;background:var(--white);box-shadow:0 6px 0 var(--white),0 -6px 0 var(--white)}

/* about */
.about-title{left:634px;top:908px;font-size:30px;color:var(--ink)}
.about-rule{left:634px;top:950px;width:60px;height:2px;background:var(--green)}
.about-copy{left:634px;top:986px;width:434px;font-size:10.5px;line-height:18px}
.checks{position:absolute;display:grid;grid-template-columns:206px 206px;row-gap:12px;font-size:10.5px;color:#333}
.checks li{list-style:none;display:flex;align-items:center;gap:8px;white-space:nowrap}
.checks svg{flex:none}

/* services */
.svc-card{position:absolute;top:1452px;width:302px;height:385px;background:var(--white);border:1px solid #eee;box-shadow:0 2px 10px rgba(0,0,0,.05);text-align:center}
.svc-card .photo{left:9px;top:12px;width:284px;height:185px}
.svc-icon{position:absolute;left:127px;top:172px;width:48px;height:48px;border-radius:50%;background:var(--white);display:flex;align-items:center;justify-content:center}
.svc-card h3{position:absolute;top:225px;left:0;width:100%;font-size:18px;color:var(--ink)}
.svc-card p{position:absolute;top:258px;left:38px;width:226px;font-size:10.5px;line-height:20px}
.svc-arrow{position:absolute;left:136px;top:340px}

/* specialized */
.special{position:absolute;left:0;top:2015px;width:1200px;height:587px;background:#161616}
.special-photo{left:0;top:0;width:640px;height:587px;background:linear-gradient(135deg,#3a3a3a 0%,#e8e8e8 40%,#cfcfcf 60%,#1e1e1e 100%)}
.special-bar{left:628px;top:148px;width:3px;height:93px;background:var(--blue)}
.special-title{left:659px;top:138px;font-size:36px;line-height:46px;color:var(--white);white-space:nowrap}
.special-copy{left:659px;top:264px;width:400px;font-size:10.5px;line-height:19px;color:#ddd}
.special .checks{left:659px;top:328px;grid-template-columns:300px;row-gap:14px;color:var(--white)}

/* team */
.member{position:absolute;top:2785px;width:218px;height:274px}
.member .photo{left:0;top:0;width:218px;height:240px}
.member-tag{position:absolute;left:16px;top:220px;width:186px;height:54px;background:var(--white);box-shadow:0 2px 8px rgba(0,0,0,.08);text-align:center;padding-top:10px}
.member-tag b{display:block;font-family:"Marcellus",serif;font-weight:400;font-size:13px;color:var(--ink)}
.member-tag span{font-size:10.5px;color:var(--text)}
.dots{position:absolute;display:flex;gap:6px}
.dots i{width:7px;height:7px;border-radius:50%;border:1px solid var(--green);display:block}
.dots i.on{background:var(--blue);border-color:var(--blue)}

/* blog + testimonials band */
.green-band{position:absolute;left:0;top:3378px;width:1200px;height:649px;background:linear-gradient(180deg,#a9d35c 0%,#95c843 100%)}
.post{position:absolute;top:3244px;width:298px;height:324px;background:var(--white);box-shadow:0 2px 10px rgba(0,0,0,.06)}
.post .photo{left:10px;top:0;width:278px;height:170px}
.post-date{position:absolute;left:10px;top:10px;width:44px;height:44px;background:var(--blue);color:var(--white);font-size:10px;line-height:13px;padding:8px 0 0 10px}
.post h4{position:absolute;left:10px;top:186px;font-family:"Marcellus",serif;font-weight:400;font-size:13px;color:var(--ink)}
.post p{position:absolute;left:10px;top:212px;width:280px;font-size:10.5px;line-height:18px}
.post a{position:absolute;left:10px;top:290px;font-size:10.5px;color:var(--blue);text-decoration:underline}
.testi-title{color:var(--ink)}
.testi-card{position:absolute;left:292px;top:3735px;width:645px;height:210px;background:var(--white);border-radius:14px;text-align:center}
.testi-avatar{position:absolute;left:568px;top:3700px;width:66px;height:66px;border-radius:50%;background:linear-gradient(135deg,#d9d9d9,#9a9a9a);border:3px solid var(--white)}
.testi-card p{position:absolute;left:100px;top:56px;width:445px;font-size:10px;line-height:14px}
.testi-card b{position:absolute;left:0;top:112px;width:100%;font-weight:500;font-size:12px;color:var(--ink)}
.testi-card small{position:absolute;left:0;top:130px;width:100%;font-size:10.5px}
.stars{position:absolute;left:0;top:150px;width:100%;color:var(--green);font-size:10px;letter-spacing:2px}
.testi-arrow{position:absolute;top:3828px;width:26px;height:26px;border-radius:50%;background:var(--white);color:var(--green);display:flex;align-items:center;justify-content:center;font-size:14px}

/* cta */
.cta{position:absolute;left:134px;top:4130px;width:933px;height:295px;overflow:hidden}
.cta .photo{left:0;top:0;width:933px;height:295px;background:linear-gradient(90deg,#4a4a4a,#6b6b6b 50%,#3c3c3c)}
.cta h2{position:absolute;left:0;top:88px;width:100%;text-align:center;font-size:30px;color:var(--white)}
.cta h5{position:absolute;left:0;top:126px;width:100%;text-align:center;font-family:"Marcellus",serif;font-weight:400;font-size:15px;color:#eee}
.cta p{position:absolute;left:230px;top:152px;width:473px;text-align:center;font-size:10px;line-height:13px;color:#eee}
.cta-btn{left:390px;top:212px;width:140px}

/* form */
.field{position:absolute;border:1px solid #eee;border-bottom:1px solid #ddd;font-size:10px;color:#aaa;padding:14px 8px}

/* footer */
.footer{position:absolute;left:0;top:4909px;width:1200px;height:342px;background:var(--dark);color:#ddd}
.foot-head{position:absolute;font-size:11px;font-weight:600;color:var(--white);letter-spacing:.5px}
.foot-line{position:absolute;display:flex;gap:10px;font-size:10.5px;line-height:16px;color:#ddd}
.foot-card{position:absolute;left:490px;top:-18px;width:227px;height:260px;background:var(--white);clip-path:polygon(0 0,100% 0,100% 88%,50% 100%,0 88%)}
.foot-brand{position:absolute;left:0;top:84px;width:100%;display:flex;justify-content:center;align-items:center;gap:8px;font-weight:600;font-size:17px;color:var(--green)}
.foot-brand i{width:24px;height:24px;border-radius:50%;background:var(--blue)}
.socials{position:absolute;left:56px;top:158px;display:flex;gap:12px}
.socials i{display:block;width:26px;height:26px;border-radius:50%;background:#222}
.socials i:first-child{background:var(--green)}
.email{position:absolute;left:869px;top:166px;width:198px;height:28px;border-radius:14px;background:var(--white);color:#555;font-size:10px;padding:7px 16px}
.sub-btn{left:869px;top:204px;width:120px;height:28px;font-size:10.5px}
.foot-nav{position:absolute;left:0;top:296px;width:1200px;text-align:center;font-size:10.5px;color:#ddd}
.foot-nav b{color:var(--white);font-weight:600}
.copy{position:absolute;top:5268px;font-size:10px;color:#444;white-space:nowrap}
</style>
</head>
<body>

<!-- header -->
<div class="brand"><span class="mark"></span>Ledgerly Bookkeeping</div>
<nav class="nav">
  <span class="active">Home</span><span>About us</span><span>Our Services</span><span>Team</span><span>Blog</span><span>Contact us</span>
</nav>
<div class="btn quote-btn">Get A Quote
  <svg width="32" height="10" viewBox="0 0 34 10"><path d="M0 5h31M27 1l4 4-4 4" stroke="#222" stroke-width="1.4" fill="none"/></svg>
</div>

<!-- hero -->
<section class="hero">
  <div class="photo hero-photo" role="img" aria-label="Smiling businesswoman with glasses working at a desk with a calculator and computer"></div>
  <div class="abs hero-bar"></div>
  <h1 class="abs serif hero-title">Helps You To<span>Company Grow</span></h1>
  <p class="abs hero-copy">Lorem Ipsum is simply dummy text of the printing and typesetting industry has been the industry's standard dummy text ever since the 1500s.</p>
  <div class="btn hero-btn">Get Started</div>
  <div class="abs hero-count">02 <i></i></div>
  <svg class="abs" style="left:0;top:470px" width="1200" height="210" viewBox="0 0 1200 210" preserveAspectRatio="none">
    <path d="M0 210V150C250 40 560 110 760 150C960 190 1110 130 1200 60V210Z" fill="#fff"/>
    <path d="M0 200C120 150 280 140 420 160C330 140 160 150 0 180Z" fill="#8dc63f"/>
    <path d="M760 200C960 190 1110 150 1200 70V110C1110 170 960 198 760 200Z" fill="#14b3ef"/>
  </svg>
</section>

<!-- about -->
<div class="photo" style="left:0;top:890px;width:323px;height:243px;background:linear-gradient(135deg,#f1f1f1,#9fb6c9 60%,#5e6f80)" role="img" aria-label="Business people reviewing financial charts on a desk"></div>
<div class="photo" style="left:93px;top:1143px;width:237px;height:175px;background:linear-gradient(135deg,#eef5fb,#cfe3f0)" role="img" aria-label="Illustration of a magnifying glass over a report and a calculator"></div>
<div class="photo" style="left:346px;top:978px;width:227px;height:295px;background:linear-gradient(160deg,#3a3a3a,#d4d4d4 55%,#f3f3f3)" role="img" aria-label="Hand pointing a pen at a printed bar chart"></div>

<h2 class="abs serif about-title">About us</h2>
<div class="abs about-rule"></div>
<div class="abs about-copy">
  <p>Lorem Ipsum is simply dummy text of the printing and typesetting industry has been the industry's standard dummy text ever since the 1500s.</p>
  <p style="margin-top:18px">when an unknown printer took a galley of type and scrambled it to make a type specimen book. It has survived not only five centuries, but also the leap into electronic typesetting, remaining essentially unchanged. It was popularised in the 1960s</p>
</div>
<ul class="checks" style="left:634px;top:1128px">
  <li><svg width="16" height="16" viewBox="0 0 16 16"><circle cx="8" cy="8" r="7" fill="none" stroke="#8dc63f"/><path d="M4.5 8l2.5 2.5 4.5-5" stroke="#8dc63f" stroke-width="1.5" fill="none"/></svg>Professional Team</li>
  <li><svg width="16" height="16" viewBox="0 0 16 16"><circle cx="8" cy="8" r="7" fill="none" stroke="#8dc63f"/><path d="M4.5 8l2.5 2.5 4.5-5" stroke="#8dc63f" stroke-width="1.5" fill="none"/></svg>Expert Adviser</li>
  <li><svg width="16" height="16" viewBox="0 0 16 16"><circle cx="8" cy="8" r="7" fill="none" stroke="#8dc63f"/><path d="M4.5 8l2.5 2.5 4.5-5" stroke="#8dc63f" stroke-width="1.5" fill="none"/></svg>High Savings Potential</li>
  <li><svg width="16" height="16" viewBox="0 0 16 16"><circle cx="8" cy="8" r="7" fill="none" stroke="#8dc63f"/><path d="M4.5 8l2.5 2.5 4.5-5" stroke="#8dc63f" stroke-width="1.5" fill="none"/></svg>High Savings Potential</li>
  <li><svg width="16" height="16" viewBox="0 0 16 16"><circle cx="8" cy="8" r="7" fill="none" stroke="#8dc63f"/><path d="M4.5 8l2.5 2.5 4.5-5" stroke="#8dc63f" stroke-width="1.5" fill="none"/></svg>24/7 customer Support</li>
  <li><svg width="16" height="16" viewBox="0 0 16 16"><circle cx="8" cy="8" r="7" fill="none" stroke="#8dc63f"/><path d="M4.5 8l2.5 2.5 4.5-5" stroke="#8dc63f" stroke-width="1.5" fill="none"/></svg>24/7 customer Support</li>
</ul>
<div class="btn" style="left:640px;top:1240px;width:128px">Read More</div>

<!-- services -->
<h2 class="section-title" style="top:1380px">Our Services</h2>
<p class="section-sub" style="top:1417px">What We Provide</p>

<article class="svc-card" style="left:124px">
  <div class="photo" style="background:linear-gradient(135deg,#5a5048,#c9b7a4 50%,#e6e0da)" role="img" aria-label="Advisor meeting with clients around a table"></div>
  <div class="svc-icon"><svg width="30" height="30" viewBox="0 0 30 30" fill="none" stroke="#333" stroke-width="1.3"><circle cx="15" cy="9" r="4"/><circle cx="7" cy="13" r="3"/><circle cx="23" cy="13" r="3"/><path d="M8 26c0-5 3-8 7-8s7 3 7 8M2 24c0-4 2-6 5-6M28 24c0-4-2-6-5-6"/></svg></div>
  <h3 class="serif">Expert Advisor</h3>
  <p>Lorem Ipsum is simply dummy text of the printing and typesetting industry has been the industry's standard.</p>
  <svg class="svc-arrow" width="30" height="14" viewBox="0 0 30 14"><path d="M2 7h24M20 1l6 6-6 6" stroke="#8dc63f" stroke-width="2" fill="none"/></svg>
</article>
<article class="svc-card" style="left:447px">
  <div class="photo" style="background:linear-gradient(135deg,#e9e9e9,#bfc3c6 50%,#6d6f72)" role="img" aria-label="Two consultants working together at a laptop"></div>
  <div class="svc-icon"><svg width="30" height="30" viewBox="0 0 30 30" fill="none" stroke="#333" stroke-width="1.3"><circle cx="15" cy="8" r="4"/><path d="M6 26c0-6 4-10 9-10s9 4 9 10M12 20l3 3 3-3"/></svg></div>
  <h3 class="serif">Tax Consulting</h3>
  <p>Lorem Ipsum is simply dummy text of the printing and typesetting industry has been the industry's standard.</p>
  <svg class="svc-arrow" width="30" height="14" viewBox="0 0 30 14"><path d="M2 7h24M20 1l6 6-6 6" stroke="#8dc63f" stroke-width="2" fill="none"/></svg>
</article>
<article class="svc-card" style="left:772px">
  <div class="photo" style="background:linear-gradient(135deg,#f2f2f2,#c7ccd1 50%,#8d949b)" role="img" aria-label="Hands pointing at financial documents on a desk"></div>
  <div class="svc-icon"><svg width="30" height="30" viewBox="0 0 30 30" fill="none" stroke="#333" stroke-width="1.3"><rect x="5" y="14" width="20" height="12"/><path d="M9 14V8h12v6M9 18h12M9 22h12M15 4v4"/></svg></div>
  <h3 class="serif" style="top:235px">Financial Planning</h3>
  <p style="top:268px">Lorem Ipsum is simply dummy text of the printing and typesetting industry has been the industry's standard.</p>
  <svg class="svc-arrow" width="30" height="14" viewBox="0 0 30 14"><path d="M2 7h24M20 1l6 6-6 6" stroke="#8dc63f" stroke-width="2" fill="none"/></svg>
</article>
<div class="btn" style="left:544px;top:1873px;width:130px">View More</div>

<!-- specialized -->
<section class="special">
  <div class="photo special-photo" role="img" aria-label="Calculator, clipboard, glasses and coffee cup on a dark desk"></div>
  <div class="abs special-bar"></div>
  <h2 class="abs serif special-title">We are specialized in<br>bookkeeping</h2>
  <p class="abs special-copy">Lorem Ipsum is simply dummy text of the printing and typesetting industry has been the industry's standard dummy text ever since the 1500s,</p>
  <ul class="checks">
    <li><svg width="16" height="16" viewBox="0 0 16 16"><circle cx="8" cy="8" r="7" fill="none" stroke="#fff"/><path d="M4.5 8l2.5 2.5 4.5-5" stroke="#fff" stroke-width="1.5" fill="none"/></svg>Expert Adviser</li>
    <li><svg width="16" height="16" viewBox="0 0 16 16"><circle cx="8" cy="8" r="7" fill="none" stroke="#fff"/><path d="M4.5 8l2.5 2.5 4.5-5" stroke="#fff" stroke-width="1.5" fill="none"/></svg>High Savings Potential</li>
    <li><svg width="16" height="16" viewBox="0 0 16 16"><circle cx="8" cy="8" r="7" fill="none" stroke="#fff"/><path d="M4.5 8l2.5 2.5 4.5-5" stroke="#fff" stroke-width="1.5" fill="none"/></svg>24/7 customer Support</li>
  </ul>
  <div class="btn" style="left:659px;top:435px;width:130px">Get Started</div>
</section>

<!-- team -->
<h2 class="section-title" style="top:2693px">Our Team</h2>
<p class="section-sub" style="top:2732px">Meet With Experts</p>

<div class="member" style="left:132px">
  <div class="photo" style="background:linear-gradient(180deg,#d8d8d8,#9a9a9a 60%,#3d3d4a)" role="img" aria-label="Portrait of a senior tax advisor in a suit"></div>
  <div class="member-tag"><b>Daniel Walsh</b><span>Senior Tax Advisor</span></div>
</div>
<div class="member" style="left:371px">
  <div class="photo" style="background:linear-gradient(180deg,#ececec,#bdbdbd 60%,#6a6a6a)" role="img" aria-label="Portrait of a tax advisor in an office"></div>
  <div class="member-tag"><b>Elena Porter</b><span>Tax Advisor</span></div>
</div>
<div class="member" style="left:612px">
  <div class="photo" style="background:linear-gradient(180deg,#eef3f7,#c7d3dd 60%,#8fa3b4)" role="img" aria-label="Portrait of a smiling senior tax advisor"></div>
  <div class="member-tag"><b>James Bradford</b><span>Senior Tax Advisor</span></div>
</div>
<div class="member" style="left:851px">
  <div class="photo" style="background:linear-gradient(180deg,#e4e4e4,#a9a39c 60%,#5c5650)" role="img" aria-label="Portrait of a financial consultant with glasses"></div>
  <div class="member-tag"><b>Emma Clarkson</b><span>Financial Consultant</span></div>
</div>
<div class="dots" style="left:587px;top:3096px"><i class="on"></i><i></i><i></i></div>

<!-- blog -->
<div class="green-band" role="img" aria-label="Green tinted background of financial papers"></div>
<h2 class="section-title" style="top:3154px">Our Blog</h2>
<p class="section-sub" style="top:3193px">Latest Blog &amp; Articles</p>

<article class="post" style="left:124px">
  <div class="photo" style="background:linear-gradient(135deg,#e8e8e8,#bcbcbc 50%,#7a7a7a)" role="img" aria-label="Calculator and laptop showing payroll screen"></div>
  <div class="post-date">02<br>Mar</div>
  <h4>Filling Payroll Taxes</h4>
  <p>Lorem Ipsum is simply dummy text of the printing and typesetting industry has been the industry's standard dummy text ever since the 1500s.</p>
  <a>Read More</a>
</article>
<article class="post" style="left:453px">
  <div class="photo" style="background:linear-gradient(135deg,#f3f3f3,#c6c6c6 50%,#555)" role="img" aria-label="Hand writing notes over a financial chart"></div>
  <div class="post-date">02<br>Mar</div>
  <h4>Finance Planning</h4>
  <p>Lorem Ipsum is simply dummy text of the printing and typesetting industry has been the industry's standard dummy text ever since the 1500s.</p>
  <a>Read More</a>
</article>
<article class="post" style="left:779px">
  <div class="photo" style="background:linear-gradient(135deg,#1f3147,#5d7fa3 50%,#b9c9d8)" role="img" aria-label="Business person viewing digital financial graphs"></div>
  <div class="post-date">02<br>Mar</div>
  <h4>Good Tax Planning</h4>
  <p>Lorem Ipsum is simply dummy text of the printing and typesetting industry has been the industry's standard dummy text ever since the 1500s.</p>
  <a>Read More</a>
</article>
<div class="btn" style="left:535px;top:3598px;width:136px">View More</div>

<!-- testimonials -->
<h2 class="section-title testi-title" style="top:3658px">Testimonials</h2>
<div class="testi-card">
  <p>Lorem Ipsum is simply dummy text of the printing and typesetting industry. Lorem Ipsum has been the industry's standard dummy text ever since the 1500s, when a printer took a galley of type and scrambled it to make a specimen.</p>
  <b>Nora Stanton</b>
  <small>Director</small>
  <div class="stars">★★★★★</div>
  <div class="dots" style="left:302px;top:170px"><i class="on" style="background:var(--green);border-color:var(--green)"></i><i></i><i></i></div>
</div>
<div class="testi-avatar" role="img" aria-label="Client portrait"></div>
<div class="testi-arrow" style="left:278px">‹</div>
<div class="testi-arrow" style="left:922px">›</div>

<!-- cta -->
<section class="cta">
  <div class="photo" role="img" aria-label="Darkened photo of a person writing over financial documents"></div>
  <h2 class="serif">Still Confused About Our Features ?</h2>
  <h5>Get A Consultant</h5>
  <p>Lorem Ipsum is simply dummy text of the printing and typesetting industry. Lorem Ipsum has been the industry's standard dummy text ever since the 1500s</p>
  <div class="btn cta-btn">Contact us</div>
</section>

<!-- quick contact -->
<h2 class="section-title" style="top:4482px;font-size:24px">Quick Contact</h2>
<div class="field" style="left:381px;top:4553px;width:216px;height:58px">Name*</div>
<div class="field" style="left:381px;top:4617px;width:216px;height:58px">Phone*</div>
<div class="field" style="left:381px;top:4681px;width:216px;height:58px">Email*</div>
<div class="field" style="left:604px;top:4553px;width:220px;height:186px">Message</div>
<div class="btn" style="left:530px;top:4760px;width:146px">Send</div>

<!-- footer -->
<footer class="footer">
  <div class="foot-head" style="left:192px;top:82px">CONTACT INFO</div>
  <div class="foot-line" style="left:186px;top:122px">
    <svg width="12" height="12" viewBox="0 0 12 12"><path d="M2 1l2.5 0 1 3-1.5 1c.8 1.6 1.8 2.6 3.4 3.4L8.4 7l3 1v2.5C6 10.5 1.5 6 2 1z" fill="#14b3ef"/></svg>
    <span>+00 123 456 7890</span></div>
  <div class="foot-line" style="left:186px;top:140px">
    <svg width="12" height="12" viewBox="0 0 12 12"><rect x="1" y="3" width="10" height="7" fill="#14b3ef"/><path d="M1 3l5 4 5-4" stroke="#1b1b1b" fill="none"/></svg>
    <span>hello@ledgerlybooks.com</span></div>
  <div class="foot-line" style="left:186px;top:172px">
    <svg width="12" height="12" viewBox="0 0 12 12"><path d="M6 11S2 7 2 4.5a4 4 0 018 0C10 7 6 11 6 11z" fill="#14b3ef"/><circle cx="6" cy="4.5" r="1.4" fill="#1b1b1b"/></svg>
    <span>45 Elm Row,<br>Brookvale, NY 10000</span></div>

  <div class="foot-card">
    <div class="foot-brand"><i></i>Ledgerly</div>
    <div class="socials" aria-label="Social links"><i></i><i></i><i></i><i></i></div>
  </div>

  <div class="foot-head" style="left:869px;top:82px">NEWSLETTER</div>
  <p class="abs" style="left:869px;top:116px;width:200px;font-size:10.5px;line-height:17px;color:#ddd">Enter Your Email Address here to be updated.</p>
  <div class="email">Email Address</div>
  <div class="btn sub-btn">Subscribe</div>

  <nav class="foot-nav"><b>Home</b> &nbsp;|&nbsp; About us &nbsp;|&nbsp; Our Services &nbsp;|&nbsp; Team &nbsp;|&nbsp; Blog &nbsp;|&nbsp; Contact us</nav>
</footer>
<p class="copy" style="left:134px">© 2021 <span style="color:var(--blue)">Ledgerly Bookkeeping</span> . All Rights Reserved.</p>
<p class="copy" style="left:889px">Privacy Policy &nbsp;|&nbsp; Term &amp; Conditions</p>

</body>
</html>
```